Keep Harbor Homestead. Avoid short sale, foreclosure, repossession, negative credit inquires and all other negative actions associated with your real estate.

Call 833-47-RENEW or info@keepharborhomestead.com

```html
<!DOCTYPE html>
<html lang="en">
<head>
<meta charset="utf-8">
<title>Keep Harbor Homestead – Postcard</title>
<link href="https://fonts.googleapis.com/css2?family=Montserrat:wght@700&family=Lato:wght@400;700&display=swap" rel="stylesheet">
<style>
  :root {
    --backdrop: #7f7f7f;
    --card: #ffffff;
    --ink: #111111;
    --red: #e31e25;
    --red-dark: #9e1217;
    --sepia-deep: #4a4340;
    --sepia-mid: #8c837e;
    --sepia-light: #c9c3bf;
  }
  * { margin: 0; padding: 0; box-sizing: border-box; }
  html, body { width: 1200px; height: 1200px; overflow: hidden; }
  body {
    background: var(--backdrop);
    position: relative;
    font-family: "Lato", Arial, sans-serif;
    color: var(--ink);
  }
  .postcard {
    position: absolute;
    left: 0; top: 192px;
    width: 1200px; height: 815px;
    background: var(--card);
    overflow: hidden;
  }
  .hero-photo {
    position: absolute;
    inset: 0;
    background:
      linear-gradient(90deg, rgba(255,255,255,0) 0%, rgba(255,255,255,0) 38%, rgba(255,255,255,0.85) 58%, #fff 72%),
      linear-gradient(180deg, var(--sepia-light) 0%, var(--sepia-deep) 28%, var(--sepia-mid) 45%, var(--sepia-mid) 75%, var(--sepia-deep) 100%);
  }
  .headline {
    position: absolute;
    left: 600px; top: 118px;
    font-family: "Montserrat", Arial, sans-serif;
    font-weight: 700;
    font-size: 80px;
    line-height: 100px;
    letter-spacing: -1px;
  }
  .headline .line-dark { color: var(--ink); display: block; }
  .headline .line-red { color: var(--red); display: block; }
  .benefits {
    position: absolute;
    left: 607px; top: 330px;
    width: 560px;
    list-style: none;
    display: grid;
    grid-template-columns: 262px 1fr;
    row-gap: 4px;
    font-size: 24px;
    line-height: 28px;
  }
  .benefits li { display: flex; align-items: center; gap: 10px; }
  .benefits li::before {
    content: "";
    width: 15px; height: 15px;
    border-radius: 50%;
    background: var(--red);
    flex: none;
  }
  .summary {
    position: absolute;
    left: 625px; top: 412px;
    width: 540px;
    font-size: 24px;
    line-height: 32px;
  }
  .call-button {
    position: absolute;
    left: 666px; top: 528px;
    width: 442px; height: 86px;
  }
  .call-button svg { position: absolute; inset: 0; }
  .call-button span {
    position: absolute;
    left: 30px; top: 10px;
    font-weight: 700;
    font-size: 44px;
    color: #fff;
    white-space: nowrap;
  }
  .contact-email {
    position: absolute;
    left: 688px; top: 636px;
    display: flex; align-items: center; gap: 12px;
    font-size: 25px;
  }
</style>
</head>
<body>
  <main class="postcard">
    <div class="hero-photo" role="img" aria-label="Sepia photograph of a child sitting by a country road beside a suitcase and a teddy bear"></div>

    <h1 class="headline">
      <span class="line-dark">Keep Harbor</span>
      <span class="line-red">Homestead</span>
    </h1>

    <ul class="benefits">
      <li>Avoid short sale</li>
      <li>foreclosure,</li>
      <li>repossession</li>
      <li>negative credit inquires</li>
    </ul>

    <p class="summary">and all other negative actions associated with your real estate.</p>

    <div class="call-button">
      <svg width="442" height="86" viewBox="0 0 442 86" aria-hidden="true">
        <polygon points="10,4 24,0 20,86 0,86" fill="var(--red-dark)"/>
        <polygon points="12,0 442,0 434,78 4,84" fill="var(--red)"/>
        <polygon points="4,84 434,78 432,86 0,86" fill="var(--red-dark)"/>
      </svg>
      <span>Call 833-47-RENEW</span>
    </div>

    <div class="contact-email">
      <svg width="26" height="18" viewBox="0 0 26 18" aria-hidden="true">
        <rect x="0" y="0" width="26" height="18" fill="var(--red)"/>
        <polyline points="1,1 13,10 25,1" fill="none" stroke="#fff" stroke-width="1.6"/>
        <polyline points="1,17 10,8 M16,8 25,17" fill="none" stroke="#fff" stroke-width="1.2"/>
      </svg>
      <span>info@keepharborhomestead.com</span>
    </div>
  </main>
</body>
</html>
```